Home Page Design (+50 More Pages To Winning Designer!)

We have a 50+ page website, but we're starting with the home page. The winning designer will get all 50+ pages to design as a 2nd project, so make sure you do your best!

SoarVane is in the private jet industry and needs a re-designed website.

We have created the structure for the website and content inside of Tavoni.io (THESE ARE ONLY ROUGH A.I. GENERATED WIREFRAMES AND DO NOT NEED TO BE FOLLOWED EXACTLY) - https://www.tavoni.io/app/project/P482915_qRuVwKsLm-DDtaHrYuop72XNc8fkoPzqlrhwDxHkaWm3Tq

Take the content from the 'Home Page' under the 'Wireframe' tab on the Tavoni.io link above, but feel free to re-design the page in a better way as these are only A.I. generated wireframes.

We want a DARK theme.... High quality, luxurious feel, greyscale colors. Attached is a brand guideline (BUT THIS IS NOT A 100% BRAND GUIDELINE, YOU CAN CHANGE COLORS AND FONTS AND MAKE CHANGES IF YOU HAVE BETTER IDEAS) and attached is our logo. We are also attaching some examples of other apps and websites to give you a guideline of what we're looking for for this design project.

The final design MUST communicate luxury using high-quality imagery of large cabin luxurious private jets.

ENTRIES THAT DO NOT FOLLOW THE PROJECT BRIEF WILL BE AUTOMATICALLY DISCARDED. FOLLOW THE INSTRUCTIONS!

Industry/Entity Type

Travel

Number of Pages Required

1 page

Font styles to use
Sans Serif

Colors

Designer to choose colors to be used in the design.

Requirements
Must have
• Follow wireframe and use content in wireframe (see Tavoni.io link)

```html
<!DOCTYPE html>
<html lang="en">
<head>
<meta charset="utf-8">
<title>SoarVane — Home Page Concepts</title>
<link rel="stylesheet" href="https://fonts.googleapis.com/css2?family=Manrope:wght@300;400;500;600&family=Tinos:wght@400&display=swap">
<style>
:root{
  --board:#262626;
  --screen:#1b1b1b;
  --bar:#0c0c0c;
  --ink:#f2f2f2;
  --muted:#a9a9a9;
  --gold:#c9b48c;
  --gold-soft:#b9a47c;
  --line:rgba(255,255,255,.6);
  --sans:'Manrope',sans-serif;
  --serif:'Tinos',serif;
}
*{margin:0;padding:0;box-sizing:border-box}
html,body{width:677px;height:1200px;overflow:hidden;background:var(--board)}
body{position:relative;font-family:var(--sans);color:var(--ink)}
.abs{position:absolute}
.brand-title{left:0;width:677px;top:30px;text-align:center;font-size:30px;font-weight:300;letter-spacing:.5px}
.caption{left:0;width:677px;text-align:center;font-size:12.5px;font-weight:300;color:var(--gold)}

/* mobile screens */
.mobile{position:absolute;left:264px;width:141px;background:var(--screen);border-radius:18px;overflow:hidden}
.m-logo{position:absolute;left:6px;font-size:7.5px;font-weight:400}
.m-menu{position:absolute;left:131px;width:7px}
.m-menu i{display:block;height:.7px;background:var(--ink);margin-bottom:1.6px}
.m-title{left:0;width:141px;top:50px;text-align:center;font-family:var(--serif);font-weight:400;font-size:10px;line-height:12.5px;letter-spacing:.3px}
.m-cta{left:36px;top:133px;width:68px;height:10px;border-radius:6px;background:rgba(20,20,20,.7);font-size:6.5px;font-weight:300;text-align:center;line-height:10px}
.m-rating{left:0;width:141px;top:152px;text-align:center;font-size:3.5px;color:var(--ink)}
.stars{color:var(--gold);letter-spacing:.5px}
.m-label{font-size:4.6px;font-weight:300;color:var(--ink)}
.m-more{font-size:4.3px;color:var(--gold)}
.m-tabs{left:0;width:141px;height:30px;background:var(--bar);display:flex;justify-content:space-around;padding-top:7px}
.tab{width:20px;text-align:center;font-size:2.8px;color:var(--muted)}
.tab svg{display:block;margin:0 auto 1.5px;width:9px;height:9px}
.tab.active{color:var(--ink)}

/* hero photo areas: dusk runway tones */
.runway-dusk{
  background:
    linear-gradient(180deg,rgba(0,0,0,0) 0%,rgba(0,0,0,0) 70%,rgba(12,12,12,.85) 88%,#141414 100%),
    radial-gradient(ellipse 45% 30% at 50% 62%,rgba(214,206,192,.55) 0%,rgba(140,130,116,.25) 45%,rgba(0,0,0,0) 75%),
    linear-gradient(180deg,#141312 0%,#2b2925 30%,#57524a 58%,#7b7365 66%,#2e2b27 71%,#1a1918 100%);
}
.m-hero{left:0;top:0;width:141px;height:150px}

/* flight card */
.card{position:absolute;border-radius:6px;overflow:hidden}
.card::after{content:"";position:absolute;left:0;right:0;bottom:0;height:38%;background:linear-gradient(180deg,rgba(40,40,44,0),rgba(40,40,44,.55))}
.card .times{position:absolute;left:6%;right:6%;display:flex;justify-content:space-between;align-items:flex-end;color:#fff;font-weight:300;z-index:1;line-height:1.05}
.card .code{display:block;font-weight:600}
.card .right{text-align:right}
.card .track{position:absolute;left:26%;right:26%;border-top:.6px dashed var(--line);z-index:1}
.card .hub{position:absolute;border:.8px solid rgba(255,255,255,.75);border-radius:50%;background:rgba(255,255,255,.18);z-index:1}
.card .heart{position:absolute;z-index:1}

.dubai{background:linear-gradient(180deg,#e9b9a6 0%,#c79b92 30%,#8c7c80 52%,#4e4c52 68%,#6f7a85 82%,#5a6470 100%)}
.newyork{background:linear-gradient(180deg,#b5cfe2 0%,#93b0c8 30%,#6c7f92 52%,#4a5a6c 64%,#3d6c9a 78%,#2f5a8a 100%)}
.amsterdam{background:linear-gradient(180deg,#e9c063 0%,#d4a455 25%,#8e6a4c 48%,#6b4d3c 64%,#7c6f68 82%,#5d5654 100%)}
.hamburg{background:linear-gradient(180deg,#dcb28e 0%,#a68d83 22%,#5c6476 45%,#3b4658 62%,#5a4a52 80%,#3a3744 100%)}
.paris{background:linear-gradient(180deg,#f5a66c 0%,#ef9062 35%,#d98463 55%,#a57a73 72%,#7a6f72 86%,#5e5c64 100%)}
.cabin{background:
  radial-gradient(ellipse 20% 45% at 78% 45%,rgba(250,246,238,.9),rgba(250,246,238,0) 70%),
  radial-gradient(ellipse 20% 45% at 58% 45%,rgba(245,238,226,.8),rgba(245,238,226,0) 70%),
  linear-gradient(90deg,#c9b598 0%,#a8896a 22%,#e3d6c2 42%,#b9a284 60%,#e9e1d4 80%,#8d7f72 100%)}
.cabin-dark{background:
  radial-gradient(ellipse 22% 22% at 50% 32%,#f3ede2 0%,rgba(243,237,226,0) 100%),
  radial-gradient(ellipse 60% 60% at 50% 55%,#9a7556 0%,#5c4330 45%,#231a14 90%)}
.crew{background:
  radial-gradient(ellipse 26% 55% at 48% 62%,#2d2f3c 0%,rgba(45,47,60,.6) 55%,rgba(45,47,60,0) 100%),
  linear-gradient(180deg,#e0c6a6 0%,#c4a27f 40%,#a98a6d 75%,#d1bca4 100%)}
.plane-top{background:
  radial-gradient(ellipse 42% 14% at 50% 52%,rgba(150,150,150,.55) 0%,rgba(90,90,90,.2) 60%,rgba(0,0,0,0) 100%),
  radial-gradient(ellipse 10% 45% at 50% 45%,rgba(170,170,170,.6) 0%,rgba(0,0,0,0) 100%),
  linear-gradient(180deg,#1b1b1b 0%,#2f2f2f 40%,#333 60%,#1b1b1b 100%)}

/* web */
.web{left:68px;top:480px;width:541px;height:291px;background:#2c2c2c;overflow:hidden}
.w-nav{left:0;top:0;width:541px;height:22px;background:#080808}
.pill{position:absolute;border:.8px solid #d8d8d8;border-radius:8px;height:10px;font-size:4.8px;line-height:8.5px;white-space:nowrap}
.nav-link{position:absolute;top:6px;font-size:6.5px;font-weight:400;transform:translateX(-50%);white-space:nowrap}
.w-hero{left:0;top:22px;width:541px;height:190px}
.w-title{left:0;width:541px;top:44px;text-align:center;font-family:var(--serif);font-weight:400;font-size:13.5px;line-height:15.6px;letter-spacing:.5px}
.w-cta{left:0;width:541px;top:162px;text-align:center;font-size:11px;font-weight:300}
.w-rating{left:0;width:541px;top:182px;text-align:center;font-size:6.5px;font-weight:400}
</style>
</head>
<body>

<div class="abs brand-title">SoarVane</div>

<!-- Mobile home page: hero -->
<section class="mobile" style="top:93px;height:305px" aria-label="Mobile home page">
  <div class="abs m-hero runway-dusk" role="img" aria-label="Private jet on a runway at dusk, seen head-on"></div>
  <div class="m-logo" style="top:12px">SoarVane</div>
  <div class="m-menu" style="top:16px"><i></i><i></i><i></i></div>
  <h1 class="abs m-title">FOR AN EXPERIENCE<br>BEYOND THE SKY</h1>
  <div class="abs m-cta">Explore Flights &rarr;</div>
  <div class="abs m-rating"><span class="stars">★★★★★</span> 4.9/5 base on 3244 reviews</div>

  <div class="abs m-label" style="left:4px;top:163px">Trend Flight Schedules</div>
  <div class="abs m-more" style="left:127px;top:163px">More</div>

  <div class="card dubai" style="left:4px;top:174px;width:64px;height:45px" role="img" aria-label="Dubai skyline at sunset">
    <svg class="heart" style="left:4px;top:3px" width="5" height="5" viewBox="0 0 10 10"><path d="M5 9 1.3 5.2A2.3 2.3 0 0 1 5 2.3a2.3 2.3 0 0 1 3.7 2.9Z" fill="none" stroke="#fff" stroke-width=".9"/></svg>
    <div class="track" style="top:39px"></div>
    <div class="hub" style="left:27px;top:34px;width:10px;height:10px"></div>
    <div class="times" style="bottom:3px;font-size:3.8px"><span>11.00<span class="code">DUB</span></span><span class="right">17.00<span class="code">LON</span></span></div>
  </div>
  <div class="card newyork" style="left:73px;top:174px;width:64px;height:45px" role="img" aria-label="New York harbour skyline">
    <svg class="heart" style="left:55px;top:3px" width="5" height="5" viewBox="0 0 10 10"><path d="M5 9 1.3 5.2A2.3 2.3 0 0 1 5 2.3a2.3 2.3 0 0 1 3.7 2.9Z" fill="none" stroke="#fff" stroke-width=".9"/></svg>
    <div class="track" style="top:39px"></div>
    <div class="hub" style="left:27px;top:34px;width:10px;height:10px"></div>
    <div class="times" style="bottom:3px;font-size:3.8px"><span>11.00<span class="code">DUB</span></span><span class="right">17.00<span class="code">LON</span></span></div>
  </div>

  <div class="abs m-label" style="left:4px;top:229px">Pictures of Our Jets</div>
  <div class="abs m-more" style="left:127px;top:229px">More</div>
  <div class="abs cabin" style="left:5px;top:238px;width:132px;height:37px;border-radius:4px 4px 0 0" role="img" aria-label="Cream leather jet cabin interior"></div>

  <nav class="abs m-tabs" style="top:275px">
    <div class="tab"><svg viewBox="0 0 12 12" fill="none" stroke="#ddd" stroke-width=".8"><circle cx="5" cy="5" r="3.8"/><path d="m8 8 3 3"/></svg>Search</div>
    <div class="tab"><svg viewBox="0 0 12 12" fill="none" stroke="#ddd" stroke-width=".8"><path d="M1 6.5 11 1 7 11 5.5 7.5Z"/></svg>My Flights</div>
    <div class="tab active"><svg viewBox="0 0 12 12" fill="none" stroke="#fff" stroke-width=".8"><path d="M1.5 5.5 6 1.5l4.5 4V11h-9Z"/></svg>Home</div>
    <div class="tab"><svg viewBox="0 0 12 12" fill="none" stroke="#ddd" stroke-width=".8"><rect x="1" y="3" width="10" height="7.5" rx="1"/><path d="M8 6h3v2H8Z"/></svg>Wallet</div>
    <div class="tab"><svg viewBox="0 0 12 12" fill="none" stroke="#ddd" stroke-width=".8"><circle cx="6" cy="4" r="2.5"/><path d="M1.5 11a4.5 4 0 0 1 9 0Z"/></svg>Profile</div>
  </nav>
</section>
<div class="abs caption" style="top:421px">Mobile Home Page</div>

<!-- Web home page -->
<section class="abs web" aria-label="Web home page">
  <div class="abs w-hero runway-dusk" role="img" aria-label="Private jet nose and engines on a runway at dusk"></div>
  <header class="abs w-nav">
    <div class="pill" style="left:13px;top:6px;width:69px;padding-left:25px">
      <svg style="position:absolute;left:5px;top:1.5px" width="5" height="5" viewBox="0 0 12 12" fill="none" stroke="#ddd" stroke-width="1.3"><circle cx="5" cy="5" r="3.8"/><path d="m8 8 3 3"/></svg>Search...
    </div>
    <span class="nav-link" style="left:137px">Aircraft</span>
    <span class="nav-link" style="left:181px">Programs</span>
    <span class="nav-link" style="left:270px;top:4px;font-size:10px;font-weight:300">SoarVane</span>
    <span class="nav-link" style="left:351px">Why SoarVane?</span>
    <span class="nav-link" style="left:406px">Life Style</span>
    <div class="pill" style="left:465px;top:6px;width:69px;padding-left:14px">Marcus Ellery
      <svg style="position:absolute;right:6px;top:1.5px" width="5" height="5" viewBox="0 0 12 12" fill="none" stroke="#ddd" stroke-width="1.2"><circle cx="6" cy="4" r="2.5"/><path d="M1.5 11a4.5 4 0 0 1 9 0Z"/></svg>
    </div>
  </header>
  <h1 class="abs w-title">FOR AN EXPERIENCE<br>BEYOND THE SKY</h1>
  <div class="abs w-cta">Explore Flights &rarr;</div>
  <div class="abs w-rating"><span class="stars" style="font-size:8px">★★★★★</span> <b style="font-weight:600">4.9/5</b> base on <span style="color:var(--gold)">3244</span> reviews</div>
  <div class="abs" style="left:13px;top:200px;font-size:5.8px;font-weight:300">Trend Flight Schedules</div>
  <div class="abs" style="left:513px;top:203px;font-size:6.5px;color:var(--gold)">More</div>

  <div class="card dubai" style="left:13px;top:214px;width:94px;height:66px" role="img" aria-label="Dubai skyline at sunset">
    <svg class="heart" style="left:6px;top:4px" width="7" height="7" viewBox="0 0 10 10"><path d="M5 9 1.3 5.2A2.3 2.3 0 0 1 5 2.3a2.3 2.3 0 0 1 3.7 2.9Z" fill="none" stroke="#fff" stroke-width=".9"/></svg>
    <div class="track" style="top:56px"></div>
    <div class="hub" style="left:39px;top:48px;width:17px;height:17px"></div>
    <div class="times" style="bottom:5px;font-size:5.8px"><span>11.00<span class="code">DUB</span></span><span class="right">17.00<span class="code">LON</span></span></div>
  </div>
  <div class="card newyork" style="left:120px;top:214px;width:94px;height:66px" role="img" aria-label="New York harbour skyline">
    <svg class="heart" style="left:6px;top:4px" width="7" height="7" viewBox="0 0 10 10"><path d="M5 9 1.3 5.2A2.3 2.3 0 0 1 5 2.3a2.3 2.3 0 0 1 3.7 2.9Z" fill="none" stroke="#fff" stroke-width=".9"/></svg>
    <div class="track" style="top:56px"></div>
    <div class="hub" style="left:39px;top:48px;width:17px;height:17px"></div>
    <div class="times" style="bottom:5px;font-size:5.8px"><span>08.30<span class="code">LON</span></span><span class="right">14.00<span class="code">DUB</span></span></div>
  </div>
  <div class="card amsterdam" style="left:226px;top:214px;width:94px;height:66px" role="img" aria-label="Amsterdam rooftops at golden hour">
    <svg class="heart" style="left:6px;top:4px" width="7" height="7" viewBox="0 0 10 10"><path d="M5 9 1.3 5.2A2.3 2.3 0 0 1 5 2.3a2.3 2.3 0 0 1 3.7 2.9Z" fill="none" stroke="#fff" stroke-width=".9"/></svg>
    <div class="track" style="top:56px"></div>
    <div class="hub" style="left:39px;top:48px;width:17px;height:17px"></div>
    <div class="times" style="bottom:5px;font-size:5.8px"><span>11.00<span class="code">IST</span></span><span class="right">13.00<span class="code">AMS</span></span></div>
  </div>
  <div class="card hamburg" style="left:333px;top:214px;width:94px;height:66px" role="img" aria-label="Hamburg harbour aerial view at dusk">
    <svg class="heart" style="left:6px;top:4px" width="7" height="7" viewBox="0 0 10 10"><path d="M5 9 1.3 5.2A2.3 2.3 0 0 1 5 2.3a2.3 2.3 0 0 1 3.7 2.9Z" fill="none" stroke="#fff" stroke-width=".9"/></svg>
    <div class="track" style="top:56px"></div>
    <div class="hub" style="left:39px;top:48px;width:17px;height:17px"></div>
    <div class="times" style="bottom:5px;font-size:5.8px"><span>11.00<span class="code">HAM</span></span><span class="right">17.00<span class="code">SAB</span></span></div>
  </div>
  <div class="card paris" style="left:435px;top:214px;width:94px;height:66px" role="img" aria-label="Paris skyline with tower at sunset">
    <svg class="heart" style="left:6px;top:4px" width="7" height="7" viewBox="0 0 10 10"><path d="M5 9 1.3 5.2A2.3 2.3 0 0 1 5 2.3a2.3 2.3 0 0 1 3.7 2.9Z" fill="none" stroke="#fff" stroke-width=".9"/></svg>
    <div class="track" style="top:56px"></div>
    <div class="hub" style="left:39px;top:48px;width:17px;height:17px"></div>
    <div class="times" style="bottom:5px;font-size:5.8px"><span>14.00<span class="code">GER</span></span><span class="right">15.00<span class="code">FRN</span></span></div>
  </div>
</section>
<div class="abs caption" style="top:794px">Web Home Page</div>

<!-- Mobile home page: fleet and programs -->
<section class="mobile" style="top:848px;height:303px" aria-label="Mobile home page, fleet section">
  <div class="m-logo" style="top:11px">SoarVane</div>
  <div class="m-menu" style="top:15px"><i></i><i></i><i></i></div>
  <div class="abs m-label" style="left:5px;top:28px;font-size:5px">JET | Aurelis</div>
  <div class="abs m-label" style="left:118px;top:28px;font-size:5px;white-space:nowrap">JET B | Cor</div>
  <div class="abs cabin-dark" style="left:5px;top:37px;width:107px;height:61px" role="img" aria-label="Jet cabin with cream leather seats"></div>
  <div class="abs cabin" style="left:118px;top:37px;width:23px;height:61px" role="img" aria-label="Jet cabin with dining table"></div>
  <div class="abs plane-top" style="left:0;top:98px;width:141px;height:63px" role="img" aria-label="Private jet seen from above in flight"></div>
  <h2 class="abs" style="left:0;width:141px;top:162px;text-align:center;font-family:var(--serif);font-weight:400;font-size:7.2px;line-height:9px;color:var(--gold-soft)">Flexible Ownership Options<br>Available</h2>
  <p class="abs" style="left:0;width:141px;top:183px;text-align:center;font-size:4.5px;line-height:6px;font-weight:300;color:#d5d5d5">Choose from a variety of ownership programs<br>and enjoy the freedom to fly onyour own terms.</p>
  <div class="abs crew" style="left:5px;top:204px;width:132px;height:70px;border-radius:4px 4px 0 0" role="img" aria-label="Cabin attendant welcoming guests aboard a jet"></div>
  <nav class="abs m-tabs" style="top:274px">
    <div class="tab"><svg viewBox="0 0 12 12" fill="none" stroke="#ddd" stroke-width=".8"><circle cx="5" cy="5" r="3.8"/><path d="m8 8 3 3"/></svg>Search</div>
    <div class="tab"><svg viewBox="0 0 12 12" fill="none" stroke="#ddd" stroke-width=".8"><path d="M1 6.5 11 1 7 11 5.5 7.5Z"/></svg>My Flights</div>
    <div class="tab active"><svg viewBox="0 0 12 12" fill="none" stroke="#fff" stroke-width=".8"><path d="M1.5 5.5 6 1.5l4.5 4V11h-9Z"/></svg>Home</div>
    <div class="tab"><svg viewBox="0 0 12 12" fill="none" stroke="#ddd" stroke-width=".8"><rect x="1" y="3" width="10" height="7.5" rx="1"/><path d="M8 6h3v2H8Z"/></svg>Wallet</div>
    <div class="tab"><svg viewBox="0 0 12 12" fill="none" stroke="#ddd" stroke-width=".8"><circle cx="6" cy="4" r="2.5"/><path d="M1.5 11a4.5 4 0 0 1 9 0Z"/></svg>Profile</div>
  </nav>
</section>
<div class="abs caption" style="top:1165px">Mobile Home Page</div>

</body>
</html>
```